Stationery
Bus. Card, Letter Head, Envelope, A5 Note pad, Email Signature
Professional
Dale Orwitz
Managing Member
4827 Fenwick Ridge Blvd
Suite 212-735
Morrisville, NC 27560
dale@pellowridge.com
www.pellowridge.com
Our logo is designed to be placed on a black background.
Our Logo
Here is the logo when on white background

```html
<!DOCTYPE html>
<html lang="en">
<head>
<meta charset="utf-8">
<title>QADLN Stationery Set</title>
<link href="https://fonts.googleapis.com/css2?family=Montserrat:wght@400;600;700&display=swap" rel="stylesheet">
<style>
  :root{
    --backdrop:#3b3b3c;
    --paper:#ffffff;
    --ink:#2b2b2b;
    --gold:#d9a21b;
    --orange:#e27c12;
    --steel:#8d8f92;
    --steel-light:#c9cacc;
    --black-card:#151515;
    --label:#b8b8b8;
  }
  *{box-sizing:border-box;margin:0;padding:0}
  html,body{width:1200px;height:314px;overflow:hidden}
  body{background:var(--backdrop);font-family:"Montserrat",sans-serif;position:relative}
  .piece{position:absolute}
  .label{position:absolute;font-size:6px;color:var(--label);letter-spacing:.3px;white-space:nowrap;transform:translateX(-50%)}
  .brand{display:flex;align-items:center;gap:4px;color:var(--gold);font-weight:700;letter-spacing:1px;white-space:nowrap}
  .brand .dot{border-radius:50%;background:var(--gold);flex:none}

  /* business cards */
  .section-title{position:absolute;left:122px;top:12px;font-size:7px;color:var(--label);transform:translateX(-50%)}
  .card{position:absolute;width:92px;height:46px;display:flex;align-items:center;justify-content:center;box-shadow:0 1px 3px rgba(0,0,0,.5);overflow:hidden}
  .card.white{background:var(--paper)}
  .card.black{background:var(--black-card)}
  .card .brand{font-size:7px}
  .card .brand .dot{width:8px;height:8px}
  .card .detail{position:absolute;left:7px;bottom:6px;font-size:3.8px;color:var(--ink);line-height:1.35;white-space:nowrap}
  .card.black .detail{color:#ddd}

  /* letterhead */
  .letterhead{width:228px;height:283px;top:17px;background:var(--paper);box-shadow:0 2px 5px rgba(0,0,0,.5);overflow:hidden}
  .letterhead .brand{position:absolute;left:14px;top:14px;font-size:9px}
  .letterhead .brand .dot{width:11px;height:11px}
  .letterhead .contact{position:absolute;left:86px;top:14px;font-size:4px;color:var(--ink);line-height:1.4;white-space:nowrap}
  .letterhead .watermark{position:absolute;left:74px;top:128px;width:86px;height:86px;border-radius:50%;border:6px solid rgba(217,162,27,.16)}
  .band{position:absolute;left:0;bottom:0;width:100%}
  .letterhead .footer{position:absolute;left:14px;bottom:16px;font-size:3.6px;color:var(--steel);white-space:nowrap}

  /* envelope front */
  .envelope{width:216px;height:90px;left:732px;background:var(--paper);box-shadow:0 2px 5px rgba(0,0,0,.5);overflow:hidden}
  .envelope .brand{position:absolute;left:10px;top:9px;font-size:7px}
  .envelope .brand .dot{width:9px;height:9px}
  .envelope .return{position:absolute;left:10px;top:22px;font-size:3.8px;color:var(--ink);line-height:1.35;white-space:nowrap}

  /* envelope backs */
  .env-back{left:972px;width:204px;height:88px}
</style>
</head>
<body>

<svg width="0" height="0" style="position:absolute">
  <defs><linearGradient id="goldband" x1="0" x2="1"><stop offset="0" stop-color="#e27c12"/><stop offset="1" stop-color="#d9a21b"/></linearGradient></defs>
</svg>

<!-- business cards -->
<div class="section-title">Business Card</div>
<div class="card white" style="left:24px;top:46px">
  <div class="brand"><span class="dot"></span>QADLN</div>
</div>
<div class="label" style="left:70px;top:96px">Card Front</div>
<div class="card black" style="left:124px;top:46px">
  <div class="brand"><span class="dot"></span>QADLN</div>
</div>
<div class="label" style="left:170px;top:96px">Card Back</div>
<div class="card white" style="left:24px;top:108px">
  <div class="detail">Dale Orwitz · Managing Member<br>dale@pellowridge.com</div>
</div>
<div class="label" style="left:70px;top:158px">Card Front</div>
<div class="card black" style="left:124px;top:108px">
  <div class="detail">Dale Orwitz · Managing Member<br>www.pellowridge.com</div>
</div>
<div class="label" style="left:170px;top:158px">Card Back</div>

<!-- letterheads -->
<div class="piece letterhead" style="left:228px">
  <div class="brand"><span class="dot"></span>QADLN</div>
  <div class="contact">4827 Fenwick Ridge Blvd, Suite 212-735<br>Morrisville, NC 27560</div>
  <div class="watermark" role="img" aria-label="Faint brand circle"></div>
  <div class="footer">dale@pellowridge.com · www.pellowridge.com</div>
  <svg class="band" width="228" height="12" viewBox="0 0 228 12">
    <polygon points="0,4 150,4 140,12 0,12" fill="url(#goldband)"/>
    <polygon points="154,4 228,4 228,12 144,12" fill="#8d8f92"/>
  </svg>
</div>
<div class="label" style="left:342px;top:303px">Letterhead Front</div>

<div class="piece letterhead" style="left:480px">
  <div class="watermark" role="img" aria-label="Faint brand circle" style="top:100px"></div>
  <svg class="band" width="228" height="12" viewBox="0 0 228 12">
    <polygon points="0,4 150,4 140,12 0,12" fill="url(#goldband)"/>
    <polygon points="154,4 228,4 228,12 144,12" fill="#8d8f92"/>
  </svg>
</div>
<div class="label" style="left:594px;top:303px">Letterhead Back</div>

<!-- envelope fronts -->
<div class="piece envelope" style="top:96px">
  <div class="brand"><span class="dot"></span>QADLN</div>
  <div class="return">4827 Fenwick Ridge Blvd<br>Suite 212-735<br>Morrisville, NC 27560</div>
  <svg class="band" width="216" height="9" viewBox="0 0 216 9">
    <polygon points="0,2 140,2 132,9 0,9" fill="url(#goldband)"/>
    <polygon points="144,2 216,2 216,9 136,9" fill="#8d8f92"/>
  </svg>
</div>
<div class="label" style="left:840px;top:189px">Envelope Front</div>
<div class="piece envelope" style="top:204px">
  <div class="brand"><span class="dot"></span>QADLN</div>
  <div class="return">4827 Fenwick Ridge Blvd<br>Suite 212-735<br>Morrisville, NC 27560</div>
  <svg class="band" width="216" height="9" viewBox="0 0 216 9">
    <polygon points="0,2 140,2 132,9 0,9" fill="url(#goldband)"/>
    <polygon points="144,2 216,2 216,9 136,9" fill="#8d8f92"/>
  </svg>
</div>
<div class="label" style="left:840px;top:297px">Envelope Front</div>

<!-- envelope backs -->
<svg class="piece env-back" style="top:14px" viewBox="0 0 204 88">
  <rect width="204" height="88" fill="#f2f2f2"/>
  <polygon points="0,0 204,0 102,52" fill="url(#goldband)"/>
  <circle cx="102" cy="28" r="9" fill="#1a1a1a"/>
</svg>
<svg class="piece env-back" style="top:108px" viewBox="0 0 204 88">
  <rect width="204" height="88" fill="#e6e6e6"/>
  <polygon points="0,0 204,0 102,50" fill="#8d8f92"/>
  <circle cx="102" cy="26" r="9" fill="#d9a21b"/>
</svg>
<svg class="piece env-back" style="top:198px" viewBox="0 0 204 88">
  <rect width="204" height="88" fill="#ffffff"/>
  <polygon points="0,0 204,0 102,50" fill="#f4f4f4" stroke="#c9cacc" stroke-width="1"/>
  <circle cx="102" cy="26" r="9" fill="#d9a21b"/>
</svg>
<div class="label" style="left:1074px;top:293px">Envelope Back Colours</div>

</body>
</html>
```